Fresh web design for high profile Golf Club

We need an exciting web site that serves both members and visitors. Our current site has the relevant sections and pages but lacks a visual impact. There are a number of very good looking golf websites out there and we want to look the best.
We need a site that will attract golfers from all over Australia to come to our course to enjoy one of the finest 36 hole championship courses as well as fantastic clubhouse facilities on their next golfing holiday.
The member section needs to provide relevant information pages and regular news and event updates to 3000 members. We are situated on the Murray River with over 300 days of sunshine and ideal golfing weather every year.
We would like to stay with our existing logo and colours as a theme.

Target Market(s)

Golfers looking for golf holiday packages.

Industry/Entity Type

Club

Requirements
Must have
• Must have contact number for golf package holidays. Must have button for member entry and button for visitor entry. Existing site is www.kelvaronegolf.com.au. Looking for a big improvement in the look of the home page.
Nice to have
• Would like constantly updated weather reporting from source such as weather channel.

```html
<!DOCTYPE html>
<html lang="en">
<head>
<meta charset="utf-8">
<title>Kelvarone Golf Club</title>
<link rel="stylesheet" href="https://fonts.googleapis.com/css2?family=Open+Sans:ital,wght@0,400;0,600;0,700;1,400&family=Archivo+Black&family=Oswald:wght@500&family=Alfa+Slab+One&display=swap">
<style>
:root{
  --header:#262626;
  --header-2:#303030;
  --nav-top:#fafafa;
  --nav-bottom:#d9d9d9;
  --teal:#3a9fae;
  --teal-dark:#2b8796;
  --page:#ececec;
  --ink:#1c1c1c;
  --muted:#3a3a3a;
  --link:#3fb0c4;
  --green:#6ab52c;
  --olive:#b4ac12;
  --yellow:#e6e02a;
  --bar:#d4d4d4;
  --footer:#0d0d0d;
  --footer-text:#bdbdbd;
  --purple:#9a0fcf;
  --lavender:#a77ef0;
}
*{box-sizing:border-box;margin:0;padding:0}
html,body{width:1096px;height:1200px;overflow:hidden;background:var(--page)}
body{position:relative;font-family:"Open Sans",Arial,sans-serif;color:var(--ink)}
.abs{position:absolute}

/* header */
.site-header{left:0;top:0;width:1096px;height:122px;background:linear-gradient(180deg,var(--header-2),var(--header))}
.brand{left:82px;top:32px;display:flex;align-items:center;gap:14px;color:#e8e8e8}
.brand-mark{width:58px;height:58px;border-radius:50%;background:#9ac93a}
.brand-name{font-size:21px;letter-spacing:4px;line-height:1}
.brand-sub{font-size:11px;letter-spacing:10px;margin-top:8px}
.search{left:493px;top:50px;width:225px;height:34px;display:flex}
.search-field{flex:1;background:#1f1f1f;color:#555;font-size:12px;font-style:italic;padding:10px 14px}
.search-btn{width:36px;background:#111}
.weather{top:34px;color:#fff;font-size:12px}
.weather .temp{color:var(--yellow);font-size:16px;font-style:italic;margin-top:8px;display:flex;align-items:center;gap:6px}
.weather .temp small{font-size:11px}

/* nav */
.main-nav{left:0;top:122px;width:1096px;height:42px;background:linear-gradient(180deg,var(--nav-top),var(--nav-bottom));display:flex;font-size:13px;color:#333}
.main-nav a{color:inherit;text-decoration:none;display:flex;align-items:center;justify-content:center;height:42px}
.main-nav .active{background:linear-gradient(180deg,var(--teal),var(--teal-dark));color:#fff}

/* hero */
.hero{left:0;top:164px;width:1096px;height:392px;background:linear-gradient(180deg,#6f8a3c 0%,#8ec43a 40%,#6aa828 75%,#4f8a1c 100%)}
.hero-title{left:556px;top:444px;font-family:"Archivo Black",Arial,sans-serif;font-size:30px;color:#fff;letter-spacing:.5px}
.hero-sub{left:556px;top:481px;font-size:14.5px;color:#fff;font-family:Arial,sans-serif}

/* entry bar */
.entry-bar{left:0;top:556px;width:1096px;height:42px;background:linear-gradient(180deg,#f4f4f4,#d6d6d6)}
.entry-card{top:560px;width:188px;height:57px;background:#fff;border:1px solid #ccc;padding:9px}
.entry-btn{height:36px;display:flex;align-items:center;justify-content:center;font-weight:700;font-size:13px;color:#222}
.entry-btn.member{background:var(--green)}
.entry-btn.visitor{background:var(--olive)}
.join{left:517px;top:581px;font-style:italic;font-size:14px;color:#4a4a1a}
.dots{left:908px;top:567px;display:flex;gap:9px}
.dot{width:22px;height:22px;border-radius:50%;background:linear-gradient(180deg,#f6f6f6,#cfcfcf);border:1px solid #c4c4c4}
.dot.on{background:#6ea52a;border-color:#5b8c20;display:flex;align-items:center;justify-content:center}
.dot.on::after{content:"";width:8px;height:8px;border-radius:50%;background:#173300}

/* intro */
.intro{left:90px;top:646px;width:640px;font-style:italic}
.intro h1{font-weight:400;font-size:16.5px;margin-bottom:20px}
.intro p{font-size:11.8px;line-height:13.3px;text-align:justify;margin-bottom:13px;color:var(--muted)}
.intro .more{color:var(--link);font-weight:600;margin-left:6px}
.download{left:92px;width:668px;height:45px;background:var(--bar);font-weight:700;font-size:13.5px;display:flex;align-items:center}
.pdf-icon{position:absolute;width:44px;height:48px}

/* news */
.news{left:771px;top:622px;width:250px;height:328px;background:#e7e7e7;border:1px solid #cfcfcf;border-radius:3px}
.news h2{position:absolute;left:16px;top:8px;font-weight:400;font-style:italic;font-size:20px;width:198px;border-bottom:1px solid #b9b9b9;padding-bottom:1px}
.news-photo{position:absolute;left:16px;top:58px;width:218px;height:95px;border-radius:12px;background:linear-gradient(180deg,#2c7fd0,#8fc2e8 45%,#7aa04a 75%,#3f6320)}
.news-meta{position:absolute;left:27px;top:166px;width:199px;display:flex;justify-content:space-between;font-size:11px;font-style:italic}
.news-text{position:absolute;left:27px;top:192px;width:199px;font-size:11px;line-height:12.8px;font-style:italic;text-align:justify}
.news-more{position:absolute;left:148px;top:268px;font-size:11px;font-style:italic;display:flex;align-items:center;gap:8px}
.news-more::before{content:"";width:14px;height:14px;border-radius:50%;background:#1c1c1c}
.news-rule{position:absolute;left:30px;top:297px;width:192px;border-top:1px solid #c9c9c9}

/* promos */
.promo{top:981px;height:103px}
.calcutta{left:82px;width:217px;background:#fff;border:1px solid #ddd}
.calcutta .head{background:var(--lavender);color:#fff;font-family:"Oswald",Arial,sans-serif;font-size:21px;text-align:center;height:32px;line-height:32px}
.calcutta .gala{font-family:"Oswald",Arial,sans-serif;color:#e0147a;font-size:19px;padding-left:5px;margin-top:2px}
.calcutta .gala span{font-size:12px}
.calcutta .tix{font-family:"Oswald",Arial,sans-serif;color:#26a34a;font-size:12px;text-align:center}
.calcutta .mc{margin:4px auto 0;width:124px;height:22px;border-radius:11px;background:var(--lavender);color:#fff;font-family:"Oswald",Arial,sans-serif;font-size:14px;text-align:center;line-height:22px}
.prorata{left:333px;width:209px;background:#1a86d8;border:2px solid #66b6ea;color:#fff;display:flex}
.prorata .left{width:118px;padding:6px 8px;font-size:6.5px;line-height:8px}
.prorata .left b{display:block;font-size:9px;letter-spacing:2px;margin-bottom:10px;font-weight:400}
.prorata .right{flex:1;background:#fff;color:#1a86d8;text-align:center;padding-top:2px;font-size:6px}
.prorata .right strong{display:block;font-size:14px;line-height:15px}
.prorata .right em{display:block;font-size:11px;font-style:normal;margin-bottom:4px}
.gig{left:581px;width:439px;background:var(--purple);border:1px solid #ddd;display:flex}
.gig .act{width:212px;color:#fff;font-family:"Alfa Slab One",serif;font-size:24px;line-height:32px;text-align:center;padding-top:14px}
.gig .info{flex:1;padding-top:9px}
.gig .free{color:#111;font-weight:700;font-size:14px;text-align:center;line-height:17px}
.gig .meals{background:#fff;color:var(--purple);font-weight:700;font-size:14.5px;line-height:17px;text-align:center;margin-top:2px;height:59px;padding-top:4px}

/* footer */
.site-footer{left:0;top:1100px;width:1096px;height:100px;background:var(--footer)}
.footer-mark{left:88px;top:1121px;width:60px;height:60px;border-radius:50%;background:#6f6f6f}
.footer-info{left:170px;top:1128px;font-style:italic;color:var(--footer-text);font-size:13px;line-height:16.5px;letter-spacing:.5px}
.footer-info .name{color:#e6e6e6;font-size:14px}
.social{left:755px;top:1125px;display:flex;gap:8px}
.social span{width:26px;height:26px;border-radius:50%;background:#2b2b2b;border:1px solid #444}
.copyright{left:766px;top:1171px;font-size:9.5px;font-style:italic;color:var(--footer-text)}
</style>
</head>
<body>

<header class="site-header abs">
</header>
<div class="brand abs">
  <span class="brand-mark"></span>
  <div>
    <div class="brand-name">KELVARONE</div>
    <div class="brand-sub">GOLFCLUB</div>
  </div>
</div>
<div class="search abs">
  <div class="search-field">Search</div>
  <div class="search-btn">
    <svg width="36" height="34" viewBox="0 0 36 34"><circle cx="17" cy="17" r="8" fill="none" stroke="#fff" stroke-width="2.5"/><line x1="23" y1="23" x2="29" y2="29" stroke="#fff" stroke-width="3"/></svg>
  </div>
</div>
<div class="weather abs" style="left:836px">Sunday
  <div class="temp">8<small>°C</small>
    <svg width="48" height="36" viewBox="0 0 48 36"><path d="M8 26a7 7 0 0 1 3-13 10 10 0 0 1 19 2 6 6 0 0 1 1 11z" fill="none" stroke="#fff" stroke-width="2.5"/><g stroke="#fff" stroke-width="2"><line x1="40" y1="6" x2="40" y2="10"/><line x1="44" y1="16" x2="48" y2="16"/><line x1="40" y1="22" x2="40" y2="28"/><line x1="18" y1="29" x2="18" y2="34"/><line x1="26" y1="29" x2="26" y2="34"/></g></svg>
  </div>
</div>
<div class="weather abs" style="left:942px">Monday
  <div class="temp">8<small>°C</small>
    <svg width="40" height="28" viewBox="0 0 40 28"><path d="M7 24a7 7 0 0 1 3-13 10 10 0 0 1 19 2 6 6 0 0 1 1 11z" fill="none" stroke="#fff" stroke-width="2.5"/></svg>
  </div>
</div>

<nav class="main-nav abs">
  <a href="#" style="width:166px">Home</a>
  <a href="#" class="active" style="width:110px">Membership</a>
  <a href="#" style="width:88px">Golf</a>
  <a href="#" style="width:114px">Club House</a>
  <a href="#" style="width:124px">News &amp; Events</a>
  <a href="#" style="width:124px">Golf Packages</a>
  <a href="#" style="width:102px">Kelvarone</a>
  <a href="#" style="width:84px">Gallery</a>
  <a href="#" style="width:112px">Contact Us</a>
</nav>

<div class="hero abs" role="img" aria-label="Photograph of a golfer mid swing on a green fairway lined with trees and bunkers"></div>
<div class="hero-title abs">Kelvarone Golf Club Pro Shop</div>
<div class="hero-sub abs">Stocklist of Carrick ,Sorvana,Tilmont,Bridgewell Maxline and More</div>

<div class="entry-bar abs"></div>
<div class="entry-card abs" style="left:88px"><div class="entry-btn member">Member Entry</div></div>
<div class="entry-card abs" style="left:284px"><div class="entry-btn visitor">Visitor Entry</div></div>
<div class="join abs">Join Now !</div>
<div class="dots abs"><span class="dot"></span><span class="dot on"></span><span class="dot"></span><span class="dot"></span></div>

<section class="intro abs">
  <h1>"A great golf course is just the beginning..."</h1>
  <p>There's so much to do on the beautiful Murray River.&nbsp; Discover Kelvarone's 36 Hole Championship Golf Course, glorious golden sandy beaches, Australian SportAviation aerodrome, the Historic Air Museum, walking tracks, State Forests, National Parks and so much more.&nbsp; Experience the history, charm and natural assets of this beautiful Murray River town only 3 hours drive from Melbourne at the start of the Newell Highway.</p>
  <p>The climate is better than Australia's famous Gold Coast with more than 300 days of sunshine, and mean temperatures of around 28°Celsius in January and 15°Celsius in July.</p>
  <p>Kelvarone Golf Club invites you to experience this exceptional sporting venue situated on Australia's mighty Murray River.&nbsp; Home of the Southern Pro Tour Trainee Championships this is one of Australia's best presented 36 Hole Championship Golf Courses.<span class="more">Read More</span></p>
</section>

<div class="download abs" style="top:850px;padding-left:137px">To download a copy of the Kelvarone Golf Club 2012 Annual Report</div>
<svg class="pdf-icon" style="left:156px;top:842px" viewBox="0 0 44 48" aria-hidden="true"><rect x="6" y="4" width="32" height="40" rx="3" fill="#fff" stroke="#999" transform="rotate(12 22 24)"/><rect x="12" y="6" width="24" height="11" fill="#8a8a8a" transform="rotate(12 22 24)"/><path d="M14 38 Q22 22 30 30" stroke="#d32020" stroke-width="4" fill="none"/></svg>
<div class="download abs" style="top:904px;padding-left:25px">To download a copy of the Kelvarone Golf Club 2012 Notice oF AGM</div>
<svg class="pdf-icon" style="left:652px;top:896px" viewBox="0 0 44 48" aria-hidden="true"><rect x="6" y="4" width="32" height="40" rx="3" fill="#fff" stroke="#999" transform="rotate(-12 22 24)"/><rect x="8" y="6" width="24" height="11" fill="#8a8a8a" transform="rotate(-12 22 24)"/><path d="M14 38 Q22 22 30 30" stroke="#d32020" stroke-width="4" fill="none"/></svg>

<aside class="news abs">
  <h2>Latest News</h2>
  <div class="news-photo" role="img" aria-label="Photograph of golf clubs in a bag against a blue sky"></div>
  <div class="news-meta"><span>12/10/2012</span><span>10.30pm</span></div>
  <p class="news-text">The Board of the Kelvarone Golf Club has now finalised the purchase of High Security water rights to guarantee sufficient water for the long term future of the club.</p>
  <div class="news-more">Read More</div>
  <div class="news-rule"></div>
  <svg style="position:absolute;left:118px;top:304px" width="28" height="14" viewBox="0 0 28 14" aria-hidden="true"><path d="M1 2h12L7 12z" fill="#999"/><path d="M15 12h12L21 2z" fill="#999"/></svg>
</aside>

<div class="promo calcutta abs">
  <div class="head">Spring Cup Calcutta</div>
  <div class="gala">Gala Night <span>Monday 5th Nov. 7pm</span></div>
  <div class="tix">$10 Calcutta Tickets on Sale NOW at Reception</div>
  <div class="mc">MC - Tessa Marle</div>
</div>

<div class="promo prorata abs">
  <div class="left">
    <b>KELVARONE</b>
    Full Golfing &nbsp;&nbsp;&nbsp;&nbsp; $175<br>
    Weekday Pass &nbsp;&nbsp; $137.50<br>
    Social &nbsp;&nbsp;&nbsp;&nbsp;&nbsp;&nbsp;&nbsp;&nbsp;&nbsp;&nbsp;&nbsp;&nbsp; $15<br>
    Junior &nbsp;&nbsp;&nbsp;&nbsp;&nbsp;&nbsp;&nbsp;&nbsp;&nbsp;&nbsp;&nbsp;&nbsp; $25<br>
    Conditions apply, see reception.
  </div>
  <div class="right">
    <strong>PRO-RATA</strong>
    <em>MEMBERSHIP</em>
    Period 1st October<br>to 31st December 2012<br><br>36 Championship Holes
  </div>
</div>

<div class="promo gig abs">
  <div class="act">Jimmy Ray<br>Dawson</div>
  <div class="info">
    <div class="free">Free to See<br>Saturday 1st December</div>
    <div class="meals">Main meals from $9.90ea.<br>Come for dinner and<br>stay for a great night!</div>
  </div>
</div>

<footer class="site-footer abs"></footer>
<div class="footer-mark abs"></div>
<div class="footer-info abs">
  <div class="name">Kelvarone Golf Club</div>
  Riverbend Rd, Kelvarone N.S.W. 2790<br>
  1800 555 019
</div>
<div class="social abs"><span></span><span></span><span></span><span></span></div>
<div class="copyright abs">Copyright © Kelvarone Golf Club 2011 &nbsp;&nbsp;&nbsp; / &nbsp;Sitemap</div>

</body>
</html>
```